New Letterhead Design Project

i need a logo letterhead & compliment slips for my new company the name of the company is called Harwick Civil Engineers Ltd the work we do is foundations floor slabs drainage retaining walls block paving & tarmac

Industry/Entity Type

It Company

```html
<!DOCTYPE html>
<html lang="en">
<head>
<meta charset="utf-8">
<title>Harwick Civil Engineers Ltd — Letterhead</title>
<link rel="stylesheet" href="https://fonts.googleapis.com/css2?family=Catamaran:wght@600;700&display=swap">
<style>
  :root {
    --ink: #111111;
    --paper: #ffffff;
    --rule-dark: #8b8989;
    --rule-light: #ababab;
    --shape-pale: #ededed;
    --shape-soft: #e2e2e2;
    --wave-mid: #d4d4d4;
    --wave-deep: #c6c6c6;
  }
  html, body {
    margin: 0;
    padding: 0;
    overflow: hidden;
    background: var(--paper);
  }
  .letterhead {
    position: relative;
    width: 927px;
    height: 1200px;
    overflow: hidden;
    background: var(--paper);
    font-family: "Catamaran", sans-serif;
    color: var(--ink);
  }
  .backdrop {
    position: absolute;
    inset: 0;
    width: 927px;
    height: 1200px;
  }
  .brand {
    position: absolute;
    left: 51px;
    top: 54px;
    width: 280px;
    text-align: center;
  }
  .brand-dot {
    width: 74px;
    height: 74px;
    margin: 0 auto 8px;
    border-radius: 50%;
    background: var(--ink);
  }
  .brand-name {
    margin: 0;
    font-size: 27px;
    font-weight: 700;
    line-height: 1.05;
    letter-spacing: 1px;
    text-transform: uppercase;
    color: var(--ink);
  }
  .contact {
    position: absolute;
    left: 51px;
    top: 1079px;
    margin: 0;
    font-size: 13.5px;
    font-weight: 700;
    line-height: 19px;
    font-style: normal;
  }
</style>
</head>
<body>
<div class="letterhead">
  <svg class="backdrop" viewBox="0 0 927 1200" aria-hidden="true">
    <defs>
      <radialGradient id="emblemGlow" cx="0.5" cy="0.5" r="0.5">
        <stop offset="0" stop-color="#e6e6e6"/>
        <stop offset="0.7" stop-color="#f1f1f1"/>
        <stop offset="1" stop-color="#ffffff" stop-opacity="0"/>
      </radialGradient>
    </defs>
    <!-- edge bars -->
    <rect x="0" y="0" width="927" height="20" fill="var(--ink)"/>
    <rect x="0" y="1178" width="927" height="22" fill="var(--ink)"/>

    <!-- top-right angular shapes -->
    <polygon points="850,20 927,20 927,58" fill="var(--shape-pale)"/>
    <polygon points="770,56 927,56 927,140" fill="var(--shape-pale)"/>
    <polygon points="815,140 927,140 927,210" fill="var(--shape-soft)"/>

    <!-- header rules -->
    <rect x="0" y="229" width="927" height="9" fill="var(--rule-dark)"/>
    <rect x="0" y="250" width="927" height="9" fill="var(--rule-light)"/>

    <!-- left angular shapes -->
    <polygon points="0,735 130,800 0,820" fill="var(--shape-pale)"/>
    <polygon points="0,820 85,865 0,875" fill="var(--shape-pale)"/>
    <polygon points="0,875 130,950 0,955" fill="var(--shape-pale)"/>
  </svg>

  <svg class="backdrop" viewBox="0 0 927 1200" role="img" aria-label="Faint company emblem decoration">
    <circle cx="780" cy="750" r="230" fill="url(#emblemGlow)"/>
    <circle cx="927" cy="400" r="110" fill="url(#emblemGlow)"/>
  </svg>

  <svg class="backdrop" viewBox="0 0 927 1200" aria-hidden="true">
    <!-- footer waves -->
    <path d="M0,985 C250,955 520,1000 927,1040 L927,1178 L0,1178 Z" fill="var(--shape-pale)"/>
    <path d="M0,1060 C300,1010 600,1040 927,1065 L927,1178 L0,1178 Z" fill="var(--wave-mid)"/>
    <path d="M300,1110 C520,1080 760,1090 927,1105 L927,1178 L300,1178 Z" fill="var(--shape-soft)"/>
    <rect x="0" y="1125" width="927" height="53" fill="var(--wave-deep)" opacity="0.55"/>
  </svg>

  <header class="brand">
    <div class="brand-dot"></div>
    <h1 class="brand-name">Harwick Civil<br>Engineers Ltd</h1>
  </header>

  <address class="contact">
    Address 24 Ferrow Lane, Oakridge, Dunmoor DM7 4QT<br>
    Email: harwickcivil@mailpost.co.uk<br>
    Phone: 01632 960418<br>
    Mob: 07700900562
  </address>
</div>
</body>
</html>
```